BRIGHT COLORFUL + 55 FAMILY HISTORY BROCHURE 11 x 17 bifold

11 x 17 Bifold Flyer I have given you the Layout I just need you to make it Pretty

YOU DO NOT NEED TO FOLLOW MY LAYOUT, You can but dont have too

Target Market(s)

55 year old consumers, who could choose our service of Hereditary Cancer Screening

Industry/Entity Type

Health And Wellness

Requirements
Must have
• Must be appealing to Grand Parents, must make them want to test , show lots of pictures of grand children, YOU DO NOT NEED TO FOLLOW MY LAYOUT , You can but dont have too
Nice to have
• use our colors of our logo , YOU DO NOT NEED TO FOLLOW MY LAYOUT , You can but dont have too
Should not have
• YOU DO NOT NEED TO FOLLOW MY LAYOUT, You can but dont have too

```html
<!DOCTYPE html>
<html lang="en">
<head>
<meta charset="utf-8">
<title>Hereditary Cancer Screening Brochure</title>
<link href="https://fonts.googleapis.com/css2?family=Lato:ital,wght@0,400;0,700;0,900;1,400;1,700;1,900&family=Andika:wght@700&display=swap" rel="stylesheet">
<style>
:root{
  --navy:#17225c;
  --green:#6cab2e;
  --pink:#f1647c;
  --grey:#d9dadd;
  --paper:#ffffff;
  --ink:#2b2b2b;
  --bg:#eeeeee;
}
*{box-sizing:border-box;margin:0;padding:0}
html,body{width:902px;height:1200px;overflow:hidden;background:var(--bg);font-family:'Lato',sans-serif;color:var(--ink)}
.spread{position:absolute;left:41px;width:820px;height:576px;display:flex;box-shadow:0 2px 10px rgba(0,0,0,.15)}
.spread-outside{top:16px}
.spread-inside{top:608px}
.page{position:relative;width:410px;height:576px;background:var(--paper);overflow:hidden}
.photo{position:absolute;display:block}
.framed{border:4px solid #fff;box-shadow:0 1px 6px rgba(0,0,0,.35)}
.round{border-radius:50%}
.abs{position:absolute}
.brand{display:flex;align-items:center;gap:5px;color:var(--navy);font-weight:900;font-size:11px;line-height:1.05;text-transform:uppercase}
.brand-dot{width:26px;height:26px;border-radius:50%;background:var(--navy);flex:none}
.url{position:absolute;left:0;right:0;text-align:center;font-weight:700;letter-spacing:2px;font-size:11.5px;color:var(--navy)}
/* outside left */
.cover-q{left:212px;top:70px;width:190px;text-align:center}
.cover-q h2{font-style:italic;font-weight:900;color:var(--navy);font-size:16px;line-height:1.2}
.cover-q p{font-style:italic;font-weight:700;color:var(--green);font-size:11.5px;line-height:1.25;margin-top:4px}
.impact{left:12px;top:225px;width:160px;text-align:center;font-style:italic;font-weight:700;color:var(--navy);font-size:11px;line-height:1.3}
.belief{left:30px;top:350px;width:350px;font-style:italic;color:var(--green);font-size:7.6px;line-height:1.35}
.belief strong{font-size:10px;font-weight:900}
.belief b{font-weight:900}
/* outside right */
.banner{left:0;top:29px;width:410px;height:33px;background:var(--pink);color:#fff;font-size:19px;letter-spacing:.6px;padding-left:12px;line-height:33px}
.tagline{left:0;right:0;top:68px;text-align:center;font-family:'Andika',sans-serif;color:var(--green);font-size:17px;font-weight:700}
.question{left:20px;right:20px;top:410px;text-align:center;font-weight:900;font-style:italic;color:var(--navy);font-size:14.5px;line-height:1.25}
.gift{left:118px;top:472px;width:292px;height:44px;background:var(--navy);padding:5px 10px}
.gift h3{color:#fff;font-size:12.5px;font-weight:700;letter-spacing:.3px}
.gift p{color:var(--green);font-size:9px;font-style:italic;margin-top:2px}
/* inside left */
.story-head{left:0;top:30px;height:26px;display:flex;font-weight:900;font-size:14px;color:#fff;line-height:26px}
.story-head .g{background:var(--green);padding:0 6px 0 20px}
.story-head .n{background:var(--navy);padding:0 40px 0 4px}
.body-copy{font-size:6.9px;line-height:1.36;color:#222}
.body-copy p{margin-bottom:7px}
.body-copy b{font-weight:900}
.stories{left:22px;top:64px;width:368px}
.reassure{left:230px;top:414px;width:170px;font-style:italic;color:var(--green);font-size:11.5px;font-weight:700;line-height:1.35}
.reassure p{margin-bottom:8px}
/* inside right */
.facts{left:16px;top:30px;width:380px;font-size:7.1px;line-height:1.4}
.facts-head{left:16px;top:206px;width:380px;font-style:italic;font-weight:900;font-size:13.5px;line-height:1.3}
.facts-head .n{color:var(--navy);display:block}
.facts-head .g{color:var(--green);display:block}
.inside-brand{left:58px;top:285px}
.inside-brand .brand-url{font-size:7px;font-weight:700;color:var(--navy);text-transform:none;margin-top:3px}
</style>
</head>
<body>

<section class="spread spread-outside">
  <article class="page back-cover">
    <div class="photo framed" style="left:15px;top:40px;width:196px;height:133px;background:linear-gradient(135deg,#c9d7e6,#e9d2c0 55%,#b9a58e)" role="img" aria-label="Grandfather being kissed on the cheek by his granddaughter"></div>
    <div class="abs cover-q">
      <h2>DOES CANCER<br>Run in Your Family?</h2>
      <p>A Simple Swab Could SAVE<br>a Family Members LIFE</p>
    </div>
    <div class="photo framed" style="left:174px;top:191px;width:194px;height:144px;background:linear-gradient(135deg,#6d8f4a,#8b5a3c 50%,#d8c0a0)" role="img" aria-label="Grandmother smiling as two grandchildren kiss her cheeks"></div>
    <p class="abs impact">Your decision won't just affect you. It will also impact Your Family, since your test results may Forecast Their Cancer Risks, too.</p>
    <p class="abs belief"><strong>We believe it is important to understand what can and cannot be learned with genetic testing.</strong> Genetic mutations can increase risks for certain cancers, but this does not mean cancer will definitely develop. You should be prepared to receive positive or negative results. <b>Most people receive Negative Results meaning no mutations associated with an increased risk for the Hereditary cancers.</b></p>
    <svg class="abs" style="left:0;top:430px" width="410" height="146" viewBox="0 0 410 146">
      <defs><linearGradient id="greyfade" x1="0" y1="0" x2="0" y2="1"><stop offset="0" stop-color="#e4e5e8"/><stop offset="1" stop-color="#c9cacd"/></linearGradient></defs>
      <path d="M0 76 Q250 66 410 10 L410 146 L0 146 Z" fill="url(#greyfade)"/>
      <path d="M0 8 Q130 36 240 40 Q130 72 0 70 Z" fill="var(--navy)"/>
      <path d="M0 76 Q250 66 410 10" stroke="#222" stroke-width="1.4" fill="none"/>
    </svg>
    <div class="abs brand" style="left:230px;top:452px"><span class="brand-dot"></span><span>Kinfield<br>Health<br>Group</span></div>
    <p class="url" style="top:538px">www.kinfieldscreening.com</p>
  </article>

  <article class="page front-cover">
    <h1 class="abs banner" style="font-weight:400">HEREDITARY CANCER SCREENING</h1>
    <p class="abs tagline">"The Test You Take For Them"</p>
    <div class="photo" style="left:60px;top:110px;width:340px;height:215px;border-radius:50%;background:radial-gradient(ellipse at 55% 50%,#d9b79a,#8fae5c 70%)" role="img" aria-label="An older hand holding a small child's hand"></div>
    <div class="photo round" style="left:34px;top:113px;width:110px;height:110px;border:3px solid #fff;background:linear-gradient(135deg,#e7d4c4,#b7a6a0)" role="img" aria-label="Grandmother hugging a young grandchild"></div>
    <div class="photo round" style="left:5px;top:215px;width:96px;height:110px;border:3px solid #fff;background:linear-gradient(135deg,#9bb07a,#d0b49a)" role="img" aria-label="Smiling grandfather"></div>
    <div class="photo round" style="left:64px;top:278px;width:110px;height:102px;border:3px solid #fff;background:linear-gradient(135deg,#b7c79a,#a59282)" role="img" aria-label="Grandfather cuddling a small grandson"></div>
    <div class="photo round" style="left:165px;top:285px;width:110px;height:102px;border:3px solid #fff;background:linear-gradient(135deg,#8fb269,#c7b7a0)" role="img" aria-label="Family of grandparents and grandchildren sitting on the grass"></div>
    <div class="photo round" style="left:278px;top:250px;width:110px;height:110px;border:3px solid #fff;background:linear-gradient(135deg,#d9c3ad,#8d6c5c)" role="img" aria-label="Grandmother embracing her granddaughter"></div>
    <p class="abs question">Will You give Your loved ones the information<br>to Beat Cancer in their lives ?</p>
    <div class="abs brand" style="left:12px;top:476px"><span class="brand-dot"></span><span>Kinfield<br>Health<br>Group</span></div>
    <div class="abs gift"><h3>GIVE THEM THE GIFT OF KNOWLEDGE</h3><p>knowing is better than not knowing. Knowledge is Power</p></div>
    <p class="url" style="top:532px">www.kinfieldscreening.com</p>
  </article>
</section>

<section class="spread spread-inside">
  <article class="page inside-left">
    <h2 class="abs story-head"><span class="g">GENETIC TESTING</span><span class="n">SAVED MY LIFE</span></h2>
    <div class="abs body-copy stories">
      <p><b>Genetic testing revealed</b> Daniel Marsh carried a mutation that gave him a 55 to 70 percent chance of developing stomach cancer. Early screening revealed there were 14 sites of stage 1A cancer. Once the news sunk in, he realized <b>his Mother Genetic Testing Saved His Life.</b></p>
      <p><b>Genetic Testing Saved My Life.</b> Because of my age and <b>Ashkenazi Jewish ancestry,</b> My Dr recommended Genetic Testing and they were right. I had the BRCA Gene, because of this my other two sister got tested, my younger sister was positive and my older sister was negative. <b>Now we are in control,</b> there are steps that can be taken to reduce the risks, including enhanced breast cancer screening, risk-reducing surgeries, and chemoprevention, in which drugs are used to try to reduce the risk or delay the development of cancer.</p>
      <p><b>A breast cancer survivor before age 30:</b> 'Genetic testing saved my life' Renee Holt was diagnosed with breast cancer two weeks before her 29th birthday. Holt, now 30, credits her recovery to <b>awareness of a hereditary genetic mutation</b> that predisposed her and her family to the disease. <b>After my mom tested positive for the BRCA 1 gene mutation,</b> I knew genetic testing was something that I would need. <b>Once I tested positive,</b> I was referred to a breast health clinic for <b>increased surveillance.</b> There, my medical care providers were very diligent in making sure I was watched closely. <b>Knowledge</b> is power and, in this case, <b>Genetic testing saved my life!</b></p>
      <p><b>My father had genetic testing</b> and found he had hereditary nonpolyposis colorectal cancer (HNPCC) commonly known as Lynch syndrome. My name is Carol Whitman and I am a 10-year survivor of colorectal cancer. From an early age I learned the importance of screenings and knew about signs and symptoms. <b>Following screening guidelines for individuals at an increased risk &amp; Knowing my family history saved my life!</b></p>
    </div>
    <svg class="abs" style="left:0;top:300px" width="410" height="104" viewBox="0 0 410 104">
      <path d="M0 10 Q60 70 250 72 L250 76 Q60 88 0 64 Z" fill="var(--navy)"/>
      <path d="M0 28 Q90 82 255 80 L255 96 L0 100 Z" fill="var(--navy)"/>
      <path d="M0 100 Q140 97 252 94" stroke="#333" stroke-width="1.2" fill="none"/>
    </svg>
    <div class="photo round" style="left:250px;top:308px;width:112px;height:92px;border:3px solid #fff;background:linear-gradient(135deg,#e8dccb,#b8c6d6)" role="img" aria-label="Grandfather holding a laughing grandson"></div>
    <div class="photo" style="left:0;top:404px;width:212px;height:172px;background:linear-gradient(135deg,#e8d6c6,#c9a88c 50%,#f1e5da)" role="img" aria-label="Mother and grandmother smiling over a sleeping baby"></div>
    <div class="abs reassure">
      <p>A Positive result or finding a mutation is Not a Cancer</p>
      <p>Diagnosis and does not mean you will ever develop Cancer</p>
      <p>Learning if you have an increased risk for cancer can make a difference</p>
    </div>
  </article>

  <article class="page inside-right">
    <div class="abs body-copy facts">
      <p><b>Genetic Testing</b> is done to determine whether family members without obvious illness have inherited the same mutation as a family member who is known to carry a cancer associated mutation. Meaning <b>Will You Help Your Kids &amp; Grand Children</b></p>
      <p><b>What are the benefits of testing?</b> "The Power of Knowledge" <b>Helping Younger Family Members Know if there is a Risk and Preparing for it.</b><br>Knowing if you have a genetic mutation is that you can work with your doctor to monitor and address your cancer risks. <b>According to the National Cancer Wellness Council eating 5 or more Servings of Vegetables &amp; Fruit, and Most Importantly also lowering your intake of red meat, dairy and eggs will help prevent or delay cancer.</b></p>
      <p><b>There are many benefits to getting tested,</b> regardless of the eventual result. If one of your family members — however distant — had cancer, there is a chance that you inherited a gene mutation that not only increases your personal risk of cancer, but also could be passed to the next generation. Those who are carriers of hereditary cancer gene mutations, could be at risk of getting cancer earlier in life than the general population. <b>The sooner genetic testing is done, the more likely it is that the risk can be managed appropriately.</b></p>
    </div>
    <p class="abs facts-head"><span class="n">There are many Known risk factors for Cancer.</span><span class="g">GENETICS and FAMILY HISTORY are Often Overlooked.</span></p>
    <div class="abs brand inside-brand"><span class="brand-dot"></span><span>Kinfield<br>Health<br>Group<span class="brand-url" style="display:block">www.kinfieldscreening.com</span></span></div>
    <svg class="abs" style="left:0;top:300px" width="410" height="110" viewBox="0 0 410 110">
      <path d="M0 40 Q200 95 410 20 L410 100 L0 100 Z" fill="var(--grey)" opacity=".6"/>
      <path d="M120 92 Q300 90 410 30 L410 100 L120 100 Z" fill="var(--green)"/>
    </svg>
    <div class="photo round" style="left:212px;top:248px;width:150px;height:136px;border:3px solid #fff;background:linear-gradient(135deg,#c7c1b8,#7a5a44 55%,#d2b79b)" role="img" aria-label="Grandparents with three smiling grandchildren"></div>
    <div class="photo" style="left:0;top:400px;width:410px;height:176px;background:linear-gradient(180deg,#9cc27a,#bcd3e6 45%,#d8c8b8)" role="img" aria-label="Three generations of a family smiling together outdoors"></div>
  </article>
</section>

</body>
</html>
```